Harborline Keys Realty business card design

Looking for an upscale and clean business card design and updated logo. I sell to a very high-end south Florida real estate market.
Target Market(s)
High-end real estate in south Florida real estate market
Industry/Entity Type
Real Estate Agent
Contact Information for Business Card
Harborline Keys Realty, Inc
738 West Pinecrest Ave, Suite 410/520, Fort Lauderdale, FL 33318
Carl Whitmore - Broker/Owner
954-555-0172 Direct
carlhomes@mailvista.example
Website: StayPinecrest.example
Font styles to use
Other font styles liked:
- Copperplate Gothic, Georgia, etc.
Requirements
Must have
- My photo, company name, my name and title, all info stated in Details above
Nice to have
- Luxury home design element, waterfront

```html
<!DOCTYPE html>
<html lang="en">
<head>
<meta charset="utf-8">
<title>Harborline Keys Realty – Business Card</title>
<link href="https://fonts.googleapis.com/css2?family=Sorts+Mill+Goudy&family=Montserrat:wght@400&display=swap" rel="stylesheet">
<style>
  :root {
    --backdrop: #2b2b2d;
    --card-black: #050505;
    --card-sheen: #2a2a2a;
    --gold: #f5cd45;
    --gold-soft: #f3d66a;
    --white: #ffffff;
    --ink: #1a1a1a;
    --bar-grey: #1c1c1c;
  }
  * { box-sizing: border-box; margin: 0; padding: 0; }
  html, body {
    width: 1200px; height: 1200px; overflow: hidden;
    background: var(--backdrop);
  }
  .canvas { position: relative; width: 1200px; height: 1200px; }

  .card {
    position: absolute; left: 174px; width: 878px; height: 528px;
    border-radius: 18px; overflow: hidden;
    background: linear-gradient(115deg, var(--card-black) 0%, var(--card-sheen) 30%, var(--card-black) 48%, var(--card-black) 100%);
  }
  .card--front { top: 72px; }
  .card--back { top: 628px; left: 181px; }

  .brand { position: absolute; display: flex; align-items: center; gap: 28px; }
  .brand-dot { border-radius: 50%; background: var(--gold); flex: none; }
  .brand-name {
    font-family: "Sorts Mill Goudy", Georgia, serif; color: var(--white);
    line-height: 1.25; text-align: center;
  }

  .card--front .brand { left: 110px; top: 150px; }
  .card--front .brand-dot { width: 150px; height: 150px; }
  .card--front .brand-name { font-size: 46px; }

  .front-web {
    position: absolute; left: 0; right: 0; bottom: 30px; text-align: center;
    font-family: "Montserrat", Arial, sans-serif; font-size: 21px; color: var(--white);
  }
  .front-web .accent { color: var(--gold); }

  .card--back .brand { left: 40px; top: 90px; }
  .card--back .brand-dot { width: 110px; height: 110px; }
  .card--back .brand-name { font-size: 32px; }

  .portrait {
    position: absolute; left: 473px; top: 0; right: 0; height: 426px;
    background: radial-gradient(ellipse at 55% 30%, #c99a82 0%, #8a6a5e 18%, transparent 34%),
                linear-gradient(180deg, #0b0b0b 0%, #0b0b0b 45%, #2d4d8f 70%, #243f78 100%);
  }

  .name-band {
    position: absolute; left: 0; top: 360px; width: 473px; height: 66px;
    background: linear-gradient(90deg, var(--gold) 0%, var(--gold-soft) 100%);
    padding: 4px 0 0 52px; color: var(--ink);
    font-family: "Sorts Mill Goudy", Georgia, serif;
  }
  .agent-name { font-size: 31px; line-height: 1.05; }
  .agent-title { font-size: 20px; line-height: 1.1; }

  .contact-bar {
    position: absolute; left: 0; right: 0; top: 426px; height: 60px;
    background: linear-gradient(90deg, var(--bar-grey), #0a0a0a);
    display: flex; align-items: center; justify-content: space-between;
    padding: 0 38px 0 50px;
    font-family: "Sorts Mill Goudy", Georgia, serif; font-size: 19px; color: var(--white);
  }
  .contact-item { display: flex; align-items: center; gap: 12px; white-space: nowrap; }
  .icon { width: 16px; height: 16px; fill: var(--gold); flex: none; }

  .address-band {
    position: absolute; left: 0; right: 0; top: 486px; height: 42px;
    background: linear-gradient(90deg, var(--gold-soft), var(--gold));
    display: flex; align-items: center; gap: 12px; padding-left: 50px;
    font-family: "Montserrat", Arial, sans-serif; font-size: 17px; color: var(--ink);
  }
  .address-band .icon { fill: #333; width: 16px; height: 18px; }
</style>
</head>
<body>
<main class="canvas">

  <section class="card card--front">
    <div class="brand">
      <span class="brand-dot"></span>
      <p class="brand-name">Harborline Keys<br>Realty, Inc.</p>
    </div>
    <p class="front-web">www.<span class="accent">StayPinecrest.example</span></p>
  </section>

  <section class="card card--back">
    <div class="brand">
      <span class="brand-dot"></span>
      <p class="brand-name">Harborline Keys<br>Realty, Inc.</p>
    </div>

    <div class="portrait" role="img" aria-label="Portrait photo of the broker in a blue checked blazer and pink shirt"></div>

    <div class="name-band">
      <p class="agent-name">Carl Whitmore</p>
      <p class="agent-title">Broker/Owner</p>
    </div>

    <div class="contact-bar">
      <span class="contact-item">
        <svg class="icon" viewBox="0 0 16 16" aria-hidden="true"><path d="M3 1h3l1.5 4-2 1.5a9 9 0 0 0 4 4L11 8.5l4 1.5v3a2 2 0 0 1-2 2A12 12 0 0 1 1 3a2 2 0 0 1 2-2z"/></svg>
        954-555-0172
      </span>
      <span class="contact-item">
        <svg class="icon" viewBox="0 0 16 16" aria-hidden="true"><path d="M1 3h14v1.5L8 9 1 4.5z"/><path d="M1 6l7 4.5L15 6v7H1z"/></svg>
        carlhomes@mailvista.example
      </span>
      <span class="contact-item">
        <svg class="icon" viewBox="0 0 16 16" aria-hidden="true"><circle cx="8" cy="8" r="7"/><path d="M1 8h14M8 1c-3 3-3 11 0 14M8 1c3 3 3 11 0 14" stroke="#111" stroke-width="1" fill="none"/></svg>
        www.StayPinecrest.example
      </span>
    </div>

    <div class="address-band">
      <svg class="icon" viewBox="0 0 16 18" aria-hidden="true"><path d="M8 0a6 6 0 0 1 6 6c0 4.5-6 12-6 12S2 10.5 2 6a6 6 0 0 1 6-6zm0 3.5a2.5 2.5 0 1 0 0 5 2.5 2.5 0 0 0 0-5z"/></svg>
      738 West Pinecrest Ave,&nbsp; Suite 410/520,&nbsp; Fort Lauderdale, FL 33318
    </div>
  </section>

</main>
</body>
</html>
```